Harbor Crest Residential Business Card Design - Logo Provided

business card design - LOGO PROVIDED. private capital fund investing in: commercial real estate (apartments), asset backed lending, private credit, flexible capital

Target Market(s)

private capital: commercial real estate (apartments), asset backed lending, private credit, flexible capital

Industry/Entity Type

alternative asset management

Contact Information for Business Card

logo, name, title, phone number, email and website

Font styles to use
Sans Serif

Colors
0054AA
0677BA
7BADD7
CADEEF
E8F1F8
EB3D1F
EC4F4E
F09395
F8D3D4
FCEDEE

Requirements
Must have
• use of logo on both sides and a qr code on the back

```html
<!DOCTYPE html>
<html lang="en">
<head>
<meta charset="utf-8">
<title>Harbor Crest Residential – Business Card</title>
<link href="https://fonts.googleapis.com/css2?family=Poppins:wght@400;500;600&display=swap" rel="stylesheet">
<style>
  :root {
    --stage: #6d6e71;
    --brand-red: #de2027;
    --brand-red-deep: #b3161c;
    --brand-blue: #0054aa;
    --brand-blue-light: #cadeef;
    --paper: #eef0f1;
    --paper-mark: #dcdfe2;
    --ink: #111111;
    --white: #ffffff;
  }
  * { margin: 0; padding: 0; box-sizing: border-box; }
  html, body {
    width: 1089px; height: 1200px; overflow: hidden;
    background: var(--stage);
    font-family: "Poppins", Arial, sans-serif;
  }
  .card {
    position: absolute; left: 158px; width: 774px; height: 442px; overflow: hidden;
  }
  .card-front { top: 125px; background: var(--brand-red); }
  .card-back  { top: 612px; background: var(--paper); }

  .brand {
    position: absolute; display: flex; align-items: center; gap: 16px;
    font-weight: 600; line-height: 1.05;
  }
  .brand-square { flex: none; }
  .brand-front {
    left: 50%; top: 50%; transform: translate(-50%, -50%);
    color: var(--brand-red-deep); font-size: 60px;
  }
  .brand-front .brand-square { width: 64px; height: 64px; background: var(--brand-red-deep); }
  .brand-back {
    left: 27px; top: 44px; color: var(--brand-blue); font-size: 40px;
  }
  .brand-back .brand-square { width: 44px; height: 44px; background: var(--brand-red); }
  .brand-watermark {
    right: 14px; bottom: 36px; color: var(--paper-mark); font-size: 40px; text-align: left;
  }

  .person { position: absolute; right: 30px; top: 28px; text-align: right; }
  .person-name { font-size: 37px; line-height: 1.15; color: var(--brand-blue); font-weight: 400; }
  .person-name .first { color: var(--brand-red); font-weight: 600; }
  .person-title { font-size: 19px; font-weight: 500; color: var(--ink); margin-top: -2px; }
  .accent-bar { position: absolute; right: 0; top: 33px; width: 21px; height: 68px; background: var(--brand-red); }

  .qr-code {
    position: absolute; right: 30px; top: 128px; width: 104px; height: 104px;
    background: var(--white); border: 6px solid var(--brand-blue);
  }

  .address {
    position: absolute; left: 27px; top: 254px; font-size: 20.5px; line-height: 29px; color: var(--brand-red);
  }
  .contacts { position: absolute; left: 27px; top: 333px; list-style: none; }
  .contacts li {
    display: flex; align-items: center; gap: 12px; font-size: 21px; line-height: 28.5px; color: var(--ink);
  }
  .contacts svg { width: 20px; height: 20px; flex: none; }
</style>
</head>
<body>

<section class="card card-front">
  <div class="brand brand-front">
    <span class="brand-square"></span>
    <span>Harbor Crest<br>Residential</span>
  </div>
</section>

<section class="card card-back">
  <div class="brand brand-back">
    <span class="brand-square"></span>
    <span>Harbor Crest<br>Residential</span>
  </div>

  <div class="person">
    <p class="person-name"><span class="first">Maren</span> Solberg</p>
    <p class="person-title">Founder &amp; CEO</p>
  </div>
  <div class="accent-bar"></div>

  <div class="qr-code" role="img" aria-label="QR code linking to the company website"></div>

  <p class="address">480 Lakeshore Ave. Suite 310<br>Denton, TX 76201</p>

  <ul class="contacts">
    <li>
      <svg viewBox="0 0 24 24" aria-hidden="true"><path fill="#de2027" d="M6.6 10.8a15.1 15.1 0 0 0 6.6 6.6l2.2-2.2c.3-.3.7-.4 1-.2 1.1.4 2.3.6 3.6.6.6 0 1 .4 1 1V20c0 .6-.4 1-1 1A17 17 0 0 1 3 4c0-.6.4-1 1-1h3.5c.6 0 1 .4 1 1 0 1.3.2 2.5.6 3.6.1.3 0 .7-.2 1z"/></svg>
      (555) 214-6083
    </li>
    <li>
      <svg viewBox="0 0 24 24" aria-hidden="true"><circle cx="12" cy="12" r="9" fill="none" stroke="#de2027" stroke-width="2.2"/><path d="M3 12h18M12 3c3 3 3 15 0 18M12 3c-3 3-3 15 0 18" fill="none" stroke="#de2027" stroke-width="1.6"/></svg>
      info@yourwebsite.com
    </li>
    <li>
      <svg viewBox="0 0 24 24" aria-hidden="true"><rect x="2.5" y="5" width="19" height="14" rx="1.5" fill="#de2027"/><path d="M3 6l9 7 9-7" fill="none" stroke="#fff" stroke-width="1.6"/></svg>
      www.yourwebsite.com
    </li>
  </ul>

  <div class="brand brand-watermark">
    <span>Harbor Crest<br>Residential</span>
  </div>
</section>

</body>
</html>
```